Business Card Design Project

Bold, modern, clean business card design needed. Prefer double sided with art logo on the back. Front of card with company name logo, no art.

Target Market(s)

Our consulting company supports local, state and federal law enforcement officers. Therefore the design should be clean and direct with no flash or arrogance to it.

Industry/Entity Type

Business

```html
<!DOCTYPE html>
<html lang="en">
<head>
<meta charset="utf-8">
<title>Halvern Technologies – Business Cards</title>
<link href="https://fonts.googleapis.com/css2?family=Open+Sans:wght@400;600;700&display=swap" rel="stylesheet">
<style>
  :root {
    --backdrop: #e9e7e3;
    --card: #ffffff;
    --ink: #1d1d1f;
    --ink-soft: #55575a;
    --panel: #141416;
    --lime: #8cc63f;
    --lime-deep: #5fa11e;
    --on-panel: #f2f2f2;
  }
  * { margin: 0; padding: 0; box-sizing: border-box; }
  html, body {
    width: 1200px; height: 913px; overflow: hidden;
    background: var(--backdrop);
    font-family: "Open Sans", Arial, sans-serif;
  }
  .canvas { position: relative; width: 1200px; height: 913px; }
  .card {
    position: absolute; width: 540px; height: 308px;
    background: var(--card); overflow: hidden;
    box-shadow: 0 10px 28px rgba(0,0,0,.18);
  }
  .card--logo { left: 50px; top: 110px; }
  .card--details { left: 610px; top: 490px; }

  .wordmark {
    position: absolute; display: flex; align-items: center; gap: 12px;
    font-weight: 700; color: var(--ink); letter-spacing: 1px;
  }
  .wordmark__dot {
    width: 26px; height: 26px; border-radius: 50%; background: var(--lime);
    flex: none;
  }
  .card--logo .wordmark {
    left: 0; right: 0; top: 0; bottom: 0; justify-content: center;
    font-size: 30px;
  }
  .card--details .wordmark {
    left: 34px; top: 128px; font-size: 20px; line-height: 24px;
  }
  .wordmark__name { display: flex; flex-direction: column; }

  .swoosh { position: absolute; inset: 0; width: 100%; height: 100%; }

  .identity { position: absolute; right: 26px; top: 20px; text-align: right; }
  .identity__name { font-size: 15px; font-weight: 700; color: var(--ink); }
  .identity__role { font-size: 10.5px; color: var(--ink-soft); }

  .contact {
    position: absolute; right: 22px; top: 100px; list-style: none;
    text-align: right; color: var(--on-panel); font-size: 10px; line-height: 18px;
  }
  .contact li { display: flex; justify-content: flex-end; align-items: center; gap: 7px; }
  .contact svg { width: 9px; height: 9px; fill: var(--on-panel); flex: none; }
</style>
</head>
<body>
<main class="canvas">

  <section class="card card--logo" aria-label="Card back">
    <div class="wordmark"><span class="wordmark__dot"></span>HALVERN TECHNOLOGIES</div>
  </section>

  <section class="card card--details" aria-label="Card front">
    <svg class="swoosh" viewBox="0 0 540 308" aria-hidden="true">
      <path d="M540 55 L440 55 C375 75 370 150 315 215 C275 260 235 290 200 308 L540 308 Z" fill="var(--panel)"/>
      <path d="M436 56 C368 80 362 152 306 214 C268 258 226 288 188 308" fill="none" stroke="var(--lime)" stroke-width="7"/>
      <path d="M425 66 C365 105 350 175 295 225 C250 265 190 282 120 292" fill="none" stroke="var(--lime-deep)" stroke-width="4"/>
      <rect x="0" y="300" width="540" height="8" fill="var(--lime)"/>
    </svg>

    <div class="wordmark">
      <span class="wordmark__dot"></span>
      <span class="wordmark__name"><span>HALVERN</span><span>TECHNOLOGIES</span></span>
    </div>

    <div class="identity">
      <p class="identity__name">Your Long Name</p>
      <p class="identity__role">Managing Director</p>
    </div>

    <ul class="contact">
      <li>00.00.00.0000 <svg viewBox="0 0 10 10"><path d="M2 0h2l1 3-1.5 1a6 6 0 0 0 2.5 2.5L7 5l3 1v2a2 2 0 0 1-2 2A8 8 0 0 1 0 2a2 2 0 0 1 2-2z"/></svg></li>
      <li>00.00.00.0000 <svg viewBox="0 0 10 10"><rect x="1" y="3" width="8" height="6" rx="1"/><rect x="3" y="0" width="4" height="3"/></svg></li>
      <li>www.yourwebsite.com <svg viewBox="0 0 10 10"><circle cx="5" cy="5" r="5"/></svg></li>
      <li>yourname@yourwebsite.com <svg viewBox="0 0 10 10"><path d="M0 2h10v6H0z"/></svg></li>
      <li>Your Commercial or office address <svg viewBox="0 0 10 10"><path d="M5 0a3.5 3.5 0 0 1 3.5 3.5C8.5 6 5 10 5 10S1.5 6 1.5 3.5A3.5 3.5 0 0 1 5 0z"/></svg></li>
    </ul>
  </section>

</main>
</body>
</html>
```